Landing Page for our Applicants Page

Landing Page for the applicants for our FB campaign and as our company NOBLE STAFF GULF.WE OFFER JOBS IN ROYAL PALACES SO THE LANDING PAGE SHOULD REFLECT THAT. We have prepared the landing page leading page photo, logo and a landing page structure. We prefer a very classy and elegant page with not much colors - black and white and gray tones is nice with a nice photos. The main photo we have suggested and we will purchase if in case the designer will like it and we agree on the style. Here is the link to it https://www.pixvaultery.com/ae/photo/beautiful-roses-and-baroque-rococo-style-palace-in-background-gm582039174-3917205 . WE ARE OPEN TO ANY PALACE PHOTO TO ATTRACT APPLICANTS TO US

Target Market(s)

Job Applicants, cleaners, nannies, cooks, nurses, tutors

Industry/Entity Type

Recruitment

Font styles to use
Serif

Requirements
Must have
• The sections that we have suggested. Our current web site if www.prime-homecarers.com you can use the partners logos from here and clients testimonials.
Nice to have
• If you have any other landing main photo that will suit more please suggest. This is only our recommendation and we have limited designers skills :). please we like clean designs - black and white lines and gray tones. Nothing too colorful. Classy and Clean.
Should not have
• We like one color palette, not numerous colors and mixed all together.

```html
<!DOCTYPE html>
<html lang="en">
<head>
<meta charset="utf-8">
<title>Noble Staff Gulf — Apply for Royal Jobs</title>
<link href="https://fonts.googleapis.com/css2?family=Montserrat:wght@600;700;800&family=Roboto:wght@400;500;700&display=swap" rel="stylesheet">
<style>
:root{
  --ink:#1d1d1d;
  --text:#333333;
  --muted:#777777;
  --line:#d9d9d9;
  --field:#f4f4f4;
  --accent:#ea8c8c;
  --pink:#fbb6b6;
  --soft:#f6f6f6;
  --white:#ffffff;
  --shade:#bcbcbc;
}
*{margin:0;padding:0;box-sizing:border-box}
html,body{width:1200px;height:4996px;overflow:hidden}
body{position:relative;background:var(--white);font-family:"Roboto",Arial,sans-serif;color:var(--text)}
.abs{position:absolute}
.topbar{left:0;top:0;width:1200px;height:29px;background:var(--ink)}
.header{left:0;top:29px;width:1200px;height:122px;background:var(--white)}
.brand{left:84px;top:72px;font-size:12px;letter-spacing:1px;color:var(--text);display:flex;align-items:center;gap:6px}
.brand .mark{width:9px;height:9px;background:var(--text)}
.nav{top:83px;font-size:15px;color:var(--ink)}
.social-top{top:84px;left:990px;display:flex;gap:12px;font-size:12px;font-weight:700;color:var(--ink)}
.hero{left:0;top:151px;width:1200px;height:593px;background:linear-gradient(180deg,#8fa6b6 0%,#c9b998 30%,#a89a78 48%,#6d7a4f 66%,#8c3d4c 80%,#4f5e36 100%)}
.hero-title{left:0;top:382px;width:1200px;text-align:center;font-family:"Montserrat",sans-serif;font-weight:600;font-size:54px;line-height:70px;color:var(--white);letter-spacing:-1px}
.perk{top:830px;width:200px;text-align:center}
.perk svg{display:block;margin:0 auto}
.perk span{display:block;margin-top:12px;font-size:10px;font-weight:500;color:var(--ink)}
.section-title{left:0;width:1200px;text-align:center;font-family:"Montserrat",sans-serif;font-weight:700;font-size:21px;color:var(--ink)}
.rule{left:532px;width:136px;height:3px;background:var(--accent)}
.apply-title{left:87px;top:1333px;font-family:"Montserrat",sans-serif;font-weight:800;font-size:40px;line-height:46px;color:var(--ink)}
.form-card{left:510px;top:1227px;width:601px;height:591px;background:var(--white);box-shadow:0 4px 22px rgba(0,0,0,.1)}
.label{left:558px;font-size:17px;font-weight:500;color:var(--ink)}
.label small{font-size:9px;font-weight:400;margin-left:10px;vertical-align:4px}
.field{left:558px;width:471px;background:var(--field);border-bottom:1px solid var(--shade)}
.send{left:853px;top:1716px;width:176px;height:54px;background:var(--accent);color:var(--white);font-size:20px;font-weight:700;display:flex;align-items:center;justify-content:center;gap:24px;box-shadow:0 2px 6px rgba(0,0,0,.15)}
.positions{top:2195px;font-size:19px;line-height:48.5px;color:var(--ink)}
.cert-band{left:0;top:2633px;width:1200px;height:577px;background:var(--soft)}
.cert-art{left:213px;top:2850px;width:243px;height:232px;border-radius:50%;background:radial-gradient(circle,#c9d4f5 0%,#dde4fb 55%,var(--soft) 72%)}
.cert-text{left:595px;top:2838px;font-family:"Montserrat",sans-serif;font-weight:800;font-size:36px;line-height:53px;color:var(--ink)}
.partner{top:3428px;height:38px;background:var(--shade);opacity:.55}
.quote-band{left:0;top:3639px;width:1200px;height:554px;background:var(--pink)}
.quote-title{left:347px;top:3763px;font-family:"Montserrat",sans-serif;font-weight:700;font-size:21px;color:var(--ink)}
.bubble{left:155px;top:3850px;width:126px;height:112px;background:var(--white);border-radius:60% 55% 50% 15%}
.bubble span{position:absolute;left:38px;top:4px;font-family:"Montserrat",sans-serif;font-weight:800;font-size:90px;color:var(--ink)}
.quote-text{left:347px;top:3860px;width:720px;font-size:21px;line-height:29px;color:var(--ink)}
.dots{left:188px;top:4073px;display:flex;gap:14px}
.dots i{width:12px;height:12px;border-radius:50%;background:#8a8a8a}
.dots i:first-child{background:var(--ink)}
.q-rule{left:632px;top:4053px;width:101px;height:3px;background:var(--ink)}
.q-name{left:632px;top:4084px;font-size:26px;font-weight:700;color:var(--ink)}
.q-place{left:632px;top:4128px;font-size:14px;color:var(--ink)}
.msg-card{left:136px;top:4385px;width:347px;height:370px;background:var(--white);box-shadow:0 3px 16px rgba(0,0,0,.1)}
.msg-card h3{position:absolute;left:49px;top:46px;font-size:17px;font-weight:500;color:var(--ink)}
.mlabel{position:absolute;left:57px;font-size:10px;font-weight:700;color:var(--ink)}
.minput{position:absolute;left:57px;width:218px;height:28px;border:1px solid var(--line);font-size:9px;color:#aaa;padding:8px 6px}
.mbtn{position:absolute;left:57px;top:298px;width:114px;height:32px;background:var(--ink);color:var(--white);font-size:10px;font-weight:700;display:flex;align-items:center;justify-content:center}
.office-title{top:4388px;font-size:22px;font-weight:500;color:var(--ink)}
.office-row{display:flex;align-items:center;gap:14px;font-size:12px;line-height:15px;color:var(--ink)}
.mail-label{left:618px;top:4644px;font-size:11px;font-weight:500;color:var(--ink)}
.mail-box{left:618px;top:4672px;width:324px;height:54px;background:var(--white);box-shadow:0 2px 10px rgba(0,0,0,.12);display:flex;align-items:center}
.mail-box .cell{padding:0 14px;font-size:13px;color:var(--ink)}
.mail-box .cell b{display:block;font-size:6px;font-weight:400;color:var(--muted);margin-bottom:4px;letter-spacing:.3px}
.mail-box .sep{width:1px;height:34px;background:var(--line)}
.social-foot{left:0;top:4852px;width:1200px;display:flex;justify-content:center;gap:22px;font-size:15px;font-weight:700;color:var(--ink)}
.footer{left:0;top:4918px;width:1200px;height:78px;background:var(--ink);color:var(--white);font-size:14px;font-weight:500}
.footer span{position:absolute;top:30px}
</style>
</head>
<body>
<div class="abs topbar"></div>
<header class="abs header"></header>
<div class="abs brand"><i class="mark"></i>NOBLE STAFF GULF</div>
<nav>
  <span class="abs nav" style="left:345px">About</span>
  <span class="abs nav" style="left:421px">Clients</span>
  <span class="abs nav" style="left:502px">Our Services</span>
  <span class="abs nav" style="left:628px">Recruitment</span>
  <span class="abs nav" style="left:754px">Training</span>
  <span class="abs nav" style="left:845px">Blog</span>
  <span class="abs nav" style="left:909px">Contact</span>
</nav>
<div class="abs social-top"><span>Kite</span><span>Wall</span><span>Nest</span><span>Orbit</span><span>Lens</span></div>

<div class="abs hero" role="img" aria-label="Photo of red roses in front of a baroque palace under a pale sky"></div>
<h1 class="abs hero-title">APPLY FOR ROYAL JOBS IN<br>DUBAI</h1>

<div class="abs perk" style="left:68px">
  <svg width="64" height="64" viewBox="0 0 64 64" fill="none" stroke="#1d1d1d" stroke-width="2"><rect x="6" y="34" width="42" height="22"/><circle cx="27" cy="45" r="6"/><path d="M12 30 L26 18 L34 24 L52 8 M44 8 H52 V16"/></svg>
  <span>SALARY STARTING 400$ NET</span>
</div>
<div class="abs perk" style="left:258px">
  <svg width="64" height="64" viewBox="0 0 64 64" fill="none" stroke="#1d1d1d" stroke-width="2"><rect x="14" y="10" width="30" height="44" rx="2"/><circle cx="29" cy="28" r="8"/><path d="M21 28 H37 M29 20 V36 M20 44 H38"/></svg>
  <span>PAID VISA</span>
</div>
<div class="abs perk" style="left:408px">
  <svg width="64" height="64" viewBox="0 0 64 64" fill="none" stroke="#1d1d1d" stroke-width="2"><circle cx="32" cy="32" r="28"/><circle cx="32" cy="32" r="18"/><path d="M26 22 V42 M38 22 V42"/></svg>
  <span>GIVEN FOOD + ACCOMODATION</span>
</div>
<div class="abs perk" style="left:581px">
  <svg width="64" height="64" viewBox="0 0 64 64" fill="none" stroke="#1d1d1d" stroke-width="2"><rect x="12" y="12" width="30" height="42" rx="2"/><circle cx="27" cy="30" r="7"/><path d="M42 20 L54 14 L50 40 M18 46 H36"/></svg>
  <span>VACATION +TICKET</span>
</div>
<div class="abs perk" style="left:773px">
  <svg width="64" height="64" viewBox="0 0 64 64" fill="none" stroke="#1d1d1d" stroke-width="2"><rect x="6" y="18" width="52" height="38" rx="3"/><path d="M24 18 V10 H40 V18 M32 28 V46 M23 37 H41"/></svg>
  <span>MEDICAL</span>
</div>
<div class="abs perk" style="left:932px">
  <svg width="64" height="64" viewBox="0 0 64 64" fill="none" stroke="#1d1d1d" stroke-width="2"><path d="M22 6 L12 14 L16 26 L20 24 V58 H44 V24 L48 26 L52 14 L42 6 L32 14 Z M32 14 V58"/></svg>
  <span>UNIFORMS AND TOILETRIES</span>
</div>

<h2 class="abs section-title" style="top:1080px">FREE APPLICATION FORM</h2>
<div class="abs rule" style="top:1131px"></div>

<h2 class="abs apply-title">APPLY FOR<br>ROYAL JOBS IN<br>DUBAI</h2>
<div class="abs form-card"></div>
<div class="abs label" style="top:1292px">Full Name</div>
<div class="abs field" style="top:1330px;height:48px"></div>
<div class="abs label" style="top:1400px">Email</div>
<div class="abs field" style="top:1436px;height:51px"></div>
<div class="abs label" style="top:1510px">Note<small>* not obligatory</small></div>
<div class="abs field" style="top:1549px;height:120px"></div>
<div class="abs send">Send
  <svg width="24" height="20" viewBox="0 0 24 20" fill="none" stroke="#fff" stroke-width="2.4"><path d="M2 10 H21 M13 2 L21 10 L13 18"/></svg>
</div>

<h2 class="abs section-title" style="top:2055px">POSITIONS WE HIRE</h2>
<div class="abs rule" style="top:2095px"></div>
<ul class="abs positions" style="left:143px;list-style:none">
  <li>Nannies</li><li>Chambermaid</li><li>Maternity Nurses</li><li>Butlers</li><li>House Managers</li><li>Personal Trainners</li>
</ul>
<ul class="abs positions" style="left:481px;list-style:none">
  <li>Estate Managers</li><li>Housekeepers</li><li>Private Chefs</li><li>Governess</li><li>Private Personal Assistants</li><li>Tutors</li>
</ul>
<ul class="abs positions" style="left:818px;list-style:none">
  <li>Executive Assitants</li><li>Security Staff</li><li>Yatcht Crew</li><li>Private Jet Cabin Crew</li><li>Chauffeurs</li>
</ul>

<section class="abs cert-band"></section>
<h2 class="abs section-title" style="top:2705px">FREE CERTIFICATION</h2>
<div class="abs rule" style="top:2750px"></div>
<div class="abs cert-art" role="img" aria-label="Illustration of a trainee beside a checklist on a soft blue cloud"></div>
<p class="abs cert-text">FREE TRAINING<br>PROGRAMS FOR THE<br>APPLICANTS WHO WISH<br>TO UPGRADE THEIR<br>SKILLSET</p>

<h2 class="abs section-title" style="top:3318px">OUR PARTNERS</h2>
<div class="abs rule" style="top:3367px"></div>
<div class="abs partner" style="left:97px;width:122px;border-radius:50%"></div>
<div class="abs partner" style="left:256px;width:118px"></div>
<div class="abs partner" style="left:430px;width:64px"></div>
<div class="abs partner" style="left:550px;width:134px;border-radius:19px"></div>
<div class="abs partner" style="left:772px;width:34px;border-radius:50%"></div>
<div class="abs partner" style="left:874px;width:70px;border-radius:50%"></div>
<div class="abs partner" style="left:984px;width:118px"></div>

<section class="abs quote-band"></section>
<h2 class="abs quote-title">WHAT OUR CLIENT SAY ABOUT US</h2>
<div class="abs bubble"><span>”</span></div>
<p class="abs quote-text">Lorem ipsum dolor sit amet, consectetur adipiscing elit. Vestibulum elementum ullamcorper eros et faucibus. Cras blandit id velit eu dignissim. Aenean ac eleifend est. Nunc tristique leo eget justo feugiat, vitae venenatis augue suscipit. Phasellus sodales massa non nibh imperdiet bibendum.</p>
<div class="abs dots"><i></i><i></i><i></i><i></i><i></i></div>
<div class="abs q-rule"></div>
<div class="abs q-name">Marisol T., Irish</div>
<div class="abs q-place">Based in Dubai</div>

<h2 class="abs section-title" style="top:4277px">CONTACT&nbsp; US</h2>
<div class="abs rule" style="top:4324px"></div>

<div class="abs msg-card">
  <h3>Send us a Message</h3>
  <span class="mlabel" style="top:86px">Name</span>
  <div class="minput" style="top:102px">eg. Sam Carter</div>
  <span class="mlabel" style="top:152px">Email</span>
  <div class="minput" style="top:168px">eg. yourname@mail.com</div>
  <span class="mlabel" style="top:218px">Message</span>
  <div class="minput" style="top:234px;height:34px"></div>
  <div class="mbtn">Send</div>
</div>

<div class="abs office-title" style="left:651px">Office in Dubai</div>
<div class="abs office-title" style="left:921px">Office in UK</div>

<div class="abs office-row" style="left:616px;top:4458px">
  <svg width="28" height="34" viewBox="0 0 28 34" fill="none" stroke="#1d1d1d" stroke-width="2.4"><path d="M14 32 C4 20 3 16 3 12 A11 11 0 0 1 25 12 C25 16 24 20 14 32 Z"/><circle cx="14" cy="12" r="4"/></svg>
  <span>Crest Tower.17th street<br>Palm Row lane, Dubai,UAE</span>
</div>
<div class="abs office-row" style="left:886px;top:4458px">
  <svg width="28" height="34" viewBox="0 0 28 34" fill="none" stroke="#1d1d1d" stroke-width="2.4"><path d="M14 32 C4 20 3 16 3 12 A11 11 0 0 1 25 12 C25 16 24 20 14 32 Z"/><circle cx="14" cy="12" r="4"/></svg>
  <span>Crest Tower.17th street<br>Palm Row lane, Dubai,UAE</span>
</div>
<div class="abs office-row" style="left:620px;top:4524px">
  <svg width="22" height="32" viewBox="0 0 22 32" fill="none" stroke="#1d1d1d" stroke-width="2.4"><rect x="2" y="2" width="18" height="28" rx="3"/><path d="M8 25 H14"/></svg>
  <span style="margin-left:4px">00 123456789</span>
</div>
<div class="abs office-row" style="left:890px;top:4524px">
  <svg width="22" height="32" viewBox="0 0 22 32" fill="none" stroke="#1d1d1d" stroke-width="2.4"><rect x="2" y="2" width="18" height="28" rx="3"/><path d="M8 25 H14"/></svg>
  <span style="margin-left:4px">00 123456789</span>
</div>

<div class="abs mail-label">You can mail us</div>
<div class="abs mail-box">
  <div class="cell"><b>FOR MORE INFORMATION</b>info@noblestaffgulf.com</div>
  <div class="sep"></div>
  <div class="cell"><b>CALL US</b>+41435550142</div>
</div>

<div class="abs social-foot"><span>Kite</span><span>Wall</span><span>Nest</span><span>Orbit</span><span>Lens</span></div>

<footer class="abs footer">
  <span style="left:96px">All rights Reserved. 2020. Noble Staff Gulf.pvt</span>
  <span style="left:768px">Terms of use</span>
  <span style="left:915px">Privacy</span>
  <span style="left:1035px">Contact</span>
</footer>
</body>
</html>
```